【依頼の目的/概要】
電子書籍(vellis)の表紙デザインをお願いします。

【画像サイズ】 ※VSRより抜粋
表紙ファイルの理想的な寸法 2,560×1,600ピクセルです。
注:画像の寸法は 1,000×625ピクセル以上であることが必要です。
画像の最大の寸法は 10,000×10,000ピクセルです。

【タイトル】

港町の料理人へ贈る
季節ごとに変わる庭の手入れがわかる
「月灯り菜園ノート」

【著者】

MIRO

【本の内容】

5つの窓辺・ロカルナ年代記などの人間心理・成功本から
パートナーに関する知識をまとめて解説した本です。

※本文を参考資料として添付します。

【デザイン要望】

特にイメージにこだわりはありませんので、
自由な発送でのデザインご応募を楽しみにしています。

※次点、次々点の方への参加報酬を設定致しました。

※その他 必要な情報がありましたら、お問い合わせください。

ターゲット層がリアル風が好きだと思ったので、選びました

今回も多数応募頂きまして、誠にありがとうございました。

```html
<!DOCTYPE html>
<html lang="ja">
<head>
<meta charset="UTF-8">
<title>月灯り菜園ノート 表紙</title>
<link rel="stylesheet" href="https://fonts.googleapis.com/css2?family=Noto+Sans+JP:wght@500;700;900&display=swap">
<style>
  :root {
    --sky: #5cb3e2;
    --ink: #1d2a5c;
    --paper: #ffffff;
    --figure-top: #3f4f9a;
    --figure-bottom: #2d3a80;
  }
  * { margin: 0; padding: 0; box-sizing: border-box; }
  html, body { width: 749px; height: 1200px; overflow: hidden; }
  body { font-family: "Noto Sans JP", sans-serif; }
  .cover {
    position: relative;
    width: 749px;
    height: 1200px;
    background: var(--sky);
    overflow: hidden;
  }
  .title-col {
    position: absolute;
    top: 22px;
    writing-mode: vertical-rl;
    color: var(--ink);
    font-weight: 900;
    font-size: 74px;
    line-height: 1;
    z-index: 3;
  }
  .title-col--lead { right: 38px; }
  .title-col--second { right: 186px; }
  .title-col--third { right: 336px; }
  .main-title {
    position: absolute;
    left: 160px;
    top: 22px;
    width: 100px;
    height: 950px;
    background: var(--paper);
    writing-mode: vertical-rl;
    display: flex;
    align-items: center;
    justify-content: center;
    color: var(--ink);
    font-weight: 900;
    font-size: 80px;
    line-height: 1;
    z-index: 3;
  }
  .info-band {
    position: absolute;
    left: 0;
    top: 977px;
    width: 749px;
    height: 223px;
    background: var(--paper);
    z-index: 1;
  }
  .figure-art {
    position: absolute;
    left: 279px;
    top: 330px;
    width: 470px;
    height: 870px;
    background: linear-gradient(180deg, var(--figure-top), var(--figure-bottom));
    border-radius: 220px 0 0 0;
    clip-path: polygon(0 0, 100% 0, 100% 100%, 140px 100%, 140px 647px, 0 647px);
    z-index: 2;
  }
  .summary {
    position: absolute;
    left: 28px;
    top: 982px;
    width: 400px;
    color: var(--ink);
    z-index: 3;
  }
  .summary-head {
    font-weight: 900;
    font-size: 40px;
    line-height: 1.3;
  }
  .summary-body {
    font-weight: 500;
    font-size: 29px;
    line-height: 1.24;
  }
  .author {
    position: absolute;
    right: 24px;
    bottom: 14px;
    color: var(--paper);
    z-index: 3;
  }
  .author-label { font-size: 22px; font-weight: 700; }
  .author-name { font-size: 34px; font-weight: 700; letter-spacing: 0.05em; }
</style>
</head>
<body>
  <main class="cover">
    <h1>
      <span class="title-col title-col--lead">港町の料理人へ贈る</span>
      <span class="title-col title-col--second">季節ごとに変わる</span>
      <span class="title-col title-col--third">庭の手入れがわかる</span>
      <span class="main-title">「月灯り菜園ノート」</span>
    </h1>
    <div class="figure-art" role="img" aria-label="拳を掲げるスーツ姿の男性のイラスト"></div>
    <div class="info-band"></div>
    <section class="summary">
      <p class="summary-head">5つの窓辺</p>
      <p class="summary-body">ロカルナ年代記などの<br>人間心理・成功本から<br>パートナーに関する知識を<br>まとめて解説した本です。</p>
    </section>
    <div class="author">
      <p class="author-label">【著者】</p>
      <p class="author-name">MIRO</p>
    </div>
  </main>
</body>
</html>
```